Business card and Logo for a private personal training studio

We need a business card and logo for a private personal training studio.

The studios name is "Harbour Stone Rise"
Main coloring to be a bright light blue. Looking for a crisp modern look

The front of the card is to have the

Studios name.
The Logo
Private Personal Training Studio
Kim Larden
0452 614 298

The back of the card is to have a lot of words relating to the services we offer. Please place the words vertically and horizontally using different fonts, different text sizes, different boldness and different colors to create a word picture.

Main words that need highlighting are

QVK, PILATES, BOXING, SPIN, STRENGTH, WEIGHT LOSS, BALANCE

Other words to add to the mix with less emphasis

Fitness, Conditioning, Lifestyle, Wellness, Health, Energy, Cardio, Goals, Muscle Tone, Vitality, Confidence, Attitude, Determination, Motivation, Dedication, Fun

Target Market(s)

Woman aged 30 to 60

Industry/Entity Type

Personal Trainer

Contact Information for Business Card

Harbour Stone Rise
Kim Larden
0452 614 298

Colors
0493ce
33a6d7
85cae6

```html
<!DOCTYPE html>
<html lang="en">
<head>
<meta charset="utf-8">
<title>Harbour Stone Rise – Business Card</title>
<link href="https://fonts.googleapis.com/css2?family=Arimo:wght@400&family=Carlito:wght@400&display=swap" rel="stylesheet">
<style>
  :root {
    --ink: #000000;
    --sky: #85cae6;
    --ocean: #0493ce;
    --mid-blue: #33a6d7;
    --white: #ffffff;
    --backdrop: #d9d9d9;
  }
  html, body {
    margin: 0;
    padding: 0;
    width: 1189px;
    height: 1200px;
    overflow: hidden;
    background: var(--backdrop);
  }
  .canvas {
    position: relative;
    width: 1189px;
    height: 1200px;
  }
  .card {
    position: absolute;
    left: 140px;
    width: 917px;
    height: 522px;
    background: var(--ink);
    overflow: hidden;
  }
  .card--front { top: 46px; }
  .card--back { top: 624px; }

  /* Front */
  .brand-mark {
    position: absolute;
    left: 89px;
    top: 38px;
    width: 248px;
    height: 248px;
    box-sizing: border-box;
    border: 4px solid var(--ocean);
    border-radius: 50%;
    display: flex;
    align-items: center;
    justify-content: center;
    text-align: center;
  }
  .brand-name {
    font-family: "Arimo", Arial, sans-serif;
    font-weight: 400;
    font-size: 30px;
    line-height: 1.15;
    color: var(--sky);
    margin: 0;
  }
  .tagline {
    position: absolute;
    left: 353px;
    top: 147px;
    margin: 0;
    font-family: "Arimo", Arial, sans-serif;
    font-size: 31px;
    color: var(--sky);
    white-space: nowrap;
  }
  .trainer-name {
    position: absolute;
    left: 393px;
    top: 292px;
    margin: 0;
    font-family: "Arimo", Arial, sans-serif;
    font-size: 52px;
    color: var(--white);
    white-space: nowrap;
  }
  .phone {
    position: absolute;
    left: 394px;
    top: 364px;
    display: flex;
    align-items: center;
    gap: 27px;
    font-family: "Arimo", Arial, sans-serif;
    font-size: 31px;
    color: var(--white);
  }
  .phone-icon { width: 23px; height: 23px; display: block; }
  .accent-band {
    position: absolute;
    left: 0;
    bottom: 0;
    width: 100%;
    height: 76px;
    background: var(--sky);
  }

  /* Back */
  .word-cloud {
    position: absolute;
    left: 0;
    top: 148px;
    width: 100%;
    margin: 0;
    padding: 0;
    list-style: none;
    font-family: "Carlito", Calibri, sans-serif;
    color: var(--sky);
    text-align: center;
  }
  .word-row {
    height: 64px;
    line-height: 64px;
    white-space: nowrap;
  }
  .word-row:nth-child(3) { height: 60px; line-height: 60px; }
  .word { font-size: 24px; }
  .word--key { font-size: 33px; }
</style>
</head>
<body>
<main class="canvas">
  <section class="card card--front" aria-label="Business card front">
    <div class="brand-mark">
      <p class="brand-name">Harbour<br>Stone Rise</p>
    </div>
    <p class="tagline">Private Personal Training Studio</p>
    <h1 class="trainer-name">Kim Larden</h1>
    <div class="phone">
      <svg class="phone-icon" viewBox="0 0 23 23" aria-hidden="true">
        <rect width="23" height="23" fill="var(--sky)"/>
        <path d="M8 4 L10 4 L10.5 8 L9 9 C9.5 11.5 11 13.5 13 14.5 L14 13 L18 14 L18 16.5 C18 17.5 17 18.5 15.5 18 C10 16.5 6 12 5.5 7 C5.5 5.5 6.5 4 8 4 Z" fill="var(--ink)"/>
      </svg>
      <span class="phone-number">0452 614 298</span>
    </div>
    <div class="accent-band"></div>
  </section>

  <section class="card card--back" aria-label="Business card back">
    <ul class="word-cloud">
      <li class="word-row"><span class="word word--key">QVK</span>&nbsp; <span class="word">Fitness</span> <span class="word word--key">PILATES</span> <span class="word">Conditioning</span> <span class="word word--key">BOXING</span> <span class="word">Lifestyle</span></li>
      <li class="word-row"><span class="word">Wellness</span> <span class="word word--key">SPIN</span>&nbsp; <span class="word">Health</span><span class="word word--key">STRENGTH</span> <span class="word">Energy</span>&nbsp; <span class="word word--key">BALANCE</span> <span class="word">Cardio</span></li>
      <li class="word-row"><span class="word">Goals, Muscle Tone, Vitality, Confidence, Attitude,</span></li>
      <li class="word-row"><span class="word">Determination,</span> <span class="word word--key">WEIGHT LOSS</span> <span class="word">Motivation, Dedication, Fun</span></li>
    </ul>
  </section>
</main>
</body>
</html>
```